Restaurant Menus Designs (Lunch, Brunch, Dinner and Beverage/Dessert)

We are seeking a design of our menu. We would like something fresh looking in line with popular upper scale gastro pub/restaurant chains.

Clean looking, wish to keep colour palate similar to our logo or complimentary scheme. Like the black background but am open to other options.

We have listed our current menus for you to use their contents only. We do not wish to have anything similar to the current menu design.

Our website is www.brackenfeld.com

Industry/Entity Type

Restaurant

Requirements
Must have
• Must have a menu for
• 11x 17" Dinner double sided
• 11x17" Lunch one side, Brunch other side Different colours than Dinner with Brunch leaning towards a brighter pallet
• 4.25 x 11 Beverage (Bar)
• 8.5x11 trifold Takeaway menu

```html
<!DOCTYPE html>
<html lang="en">
<head>
<meta charset="utf-8">
<title>Brackenfeld's Dinner Menu</title>
<link href="https://fonts.googleapis.com/css2?family=Alfa+Slab+One&family=Rozha+One&family=Archivo:wght@600;700&family=Archivo+Narrow:wght@700&display=swap" rel="stylesheet">
<style>
  :root {
    --paper: #efebe3;
    --paper-deep: #e6e1d7;
    --red: #cc3b3c;
    --ink: #3b3535;
    --salad: #9cb86a;
    --shell: #d9b98c;
    --prawn: #e0916a;
    --meat: #b98a7a;
    --bun: #d8ab6a;
  }
  * { margin: 0; padding: 0; box-sizing: border-box; }
  html, body { width: 1200px; height: 777px; overflow: hidden; background: var(--paper); }
  .menu {
    position: relative; width: 1200px; height: 777px;
    background: radial-gradient(ellipse at 50% 50%, var(--paper) 60%, var(--paper-deep) 100%);
    font-family: "Archivo Narrow", "Arial Narrow", sans-serif;
    color: var(--ink);
  }
  .art { position: absolute; border-radius: 40%; opacity: .55; z-index: 0; }
  .section-title {
    position: absolute; font-family: "Alfa Slab One", serif; color: var(--red);
    font-weight: 400; letter-spacing: 1.5px; line-height: 1; z-index: 2;
  }
  .section-title.salads { left: 122px; top: 32px; font-size: 30px; }
  .section-title.main { left: 820px; top: 27px; font-size: 36px; letter-spacing: 2px; }
  .section-title.starters {
    left: 218px; top: 402px; font-family: "Rozha One", serif; font-size: 38px;
    letter-spacing: 0; background: var(--paper); padding: 0 6px; transform: scaleX(.82); transform-origin: left;
  }
  .section-title.sides { left: 912px; top: 607px; font-size: 26px; }
  .starters-frame {
    position: absolute; left: 36px; top: 388px; width: 536px; height: 356px;
    border: 1px solid var(--red); z-index: 1;
  }
  .item { position: absolute; width: 256px; z-index: 2; }
  .item h3 {
    font-family: "Archivo", sans-serif; font-weight: 600; font-size: 14px; line-height: 15.5px;
    color: var(--red); text-transform: uppercase; letter-spacing: .4px; margin-bottom: 6px;
  }
  .item h3 .price { font-size: 9px; letter-spacing: 0; }
  .main-col .item h3 { margin-bottom: 1px; }
  .item p {
    font-size: 9.4px; line-height: 9.9px; text-transform: uppercase; letter-spacing: .15px;
  }
  .item .note { font-style: italic; padding-left: 8px; }
  .sides-list {
    position: absolute; left: 928px; top: 638px; list-style: none; z-index: 2;
    font-size: 9.6px; line-height: 10.4px; text-transform: uppercase; letter-spacing: .3px;
  }
</style>
</head>
<body>
<main class="menu">
  <div class="art" role="img" aria-label="Watercolour illustration of a leafy salad with tomato and a sliced egg" style="left:0;top:0;width:116px;height:88px;background:radial-gradient(circle at 30% 30%, var(--salad), #c7d59a 60%, transparent 75%);"></div>
  <div class="art" role="img" aria-label="Watercolour illustration of a garden salad with cucumber, tomatoes and croutons" style="left:312px;top:272px;width:176px;height:116px;background:radial-gradient(ellipse at 50% 50%, var(--salad), #d9cf9a 55%, transparent 75%);"></div>
  <div class="art" role="img" aria-label="Watercolour illustration of a halved scotch egg" style="left:0;top:368px;width:64px;height:72px;background:radial-gradient(circle, #f0b488 25%, #a87a5a 55%, transparent 72%);"></div>
  <div class="art" role="img" aria-label="Watercolour illustration of a shrimp" style="left:480px;top:612px;width:92px;height:112px;background:radial-gradient(ellipse, var(--prawn), transparent 70%);"></div>
  <div class="art" role="img" aria-label="Watercolour illustration of chicken wings and mussel shells" style="left:0;top:676px;width:232px;height:101px;background:radial-gradient(ellipse at 40% 70%, var(--shell), #7d8a9a 50%, transparent 75%);"></div>
  <div class="art" role="img" aria-label="Watercolour illustration of a sliced steak with greens and fries" style="left:596px;top:616px;width:292px;height:161px;background:radial-gradient(ellipse at 50% 70%, var(--meat), #b3c18a 50%, transparent 75%);"></div>
  <div class="art" role="img" aria-label="Watercolour illustration of grilled bread slices" style="left:968px;top:720px;width:144px;height:57px;background:radial-gradient(ellipse, #d9c8a0, transparent 72%);"></div>
  <div class="art" role="img" aria-label="Watercolour illustration of a stacked burger on a skewer" style="left:1064px;top:480px;width:136px;height:297px;background:radial-gradient(ellipse at 50% 55%, var(--bun), #8a5a45 50%, transparent 75%);"></div>

  <h2 class="section-title salads">SALADS AND SOUPS</h2>

  <section class="salads-col">
    <div class="item" style="left:40px;top:82px;">
      <h3>Garden Fresh Salad <span class="price">9</span></h3>
      <p>We've sourced the best greens and the freshest vegetables around and we're bringing them from the farms to your plate! Top with our homemade sweet tomato vinaigrette and your taste buds will be doing a wee jig.</p>
    </div>
    <div class="item" style="left:40px;top:180px;">
      <h3>Caesar Salad <span class="price">10</span></h3>
      <p>They say "Don't mess with perfection." We say "Just watch us!" We're elevating this classic with crisp romaine, maple candied bacon, Irish cheese and house made soda bread croutons all dressed with rich Caesar dressing.</p>
      <p class="note">Add chicken 4</p>
    </div>
    <div class="item" style="left:40px;top:288px;">
      <h3>Fresh Beet Salad <span class="price">12</span></h3>
      <p>"The beet goes on" with our freshly prepared beets served with a bed of peppery arugula and fresh spinach, topped with creamy goat cheese, candied walnuts and a rich, deep maple balsamic dressing.</p>
    </div>
    <div class="item" style="left:314px;top:82px;width:244px;">
      <h3>Seafood Chowder</h3>
      <p>Chock full of the freshest seafood, our rich, thick and creamy chowder is brimming with scallops, lobster, shrimp, haddock and salmon. Thickened with a buttery potato slurry.</p>
      <p class="note">Cup 8<br>Bowl 14</p>
    </div>
    <div class="item" style="left:314px;top:190px;width:244px;">
      <h3>Yesterday's Soup</h3>
      <p>Everyone knows soup is better the next day! This soup was made yesterday with the freshest ingredients; we've let the flavors meld overnight and today its perfection!</p>
      <p class="note">Cup 5<br>Bowl 8</p>
    </div>
  </section>

  <div class="starters-frame"></div>
  <h2 class="section-title starters">STARTERS</h2>

  <section class="starters-col">
    <div class="item" style="left:40px;top:448px;">
      <h3>Scotch Egg <span class="price">9</span></h3>
      <p>There's nothing better than a scotch egg! A perfectly boiled egg encased in savory sausage meat, fried until golden and served open face. Drizzled with a sweet honey and grainy mustard sauce.</p>
    </div>
    <div class="item" style="left:40px;top:536px;">
      <h3>Classic Mussels <span class="price">12</span></h3>
      <p>We take a generous 1 1/2 pound stack of fresh mussels, steam them in a buttery white wine broth add a hint of garlic and herbs then finish with green onion, absolutely awesome! Served with grilled artisan potato bread.</p>
    </div>
    <div class="item" style="left:40px;top:634px;">
      <h3>Drunken Irish Mussels <span class="price">14</span></h3>
      <p>We take mussels to a whole new level! 1 1/2 pounds of fresh mussels steamed in dark stout, then stepped up with some double smoked bacon and fresh green onion. Finished with herbs and served with grilled artisan potato bread. These mussels are divine and drunk!</p>
    </div>
    <div class="item" style="left:314px;top:448px;width:250px;">
      <h3>Smoked Chicken Wings <span class="price">15</span></h3>
      <p>These succulent wings are smoked in-house (need we say more?) and served with a house made tangy-sweet sticky glaze. We've taken this old standard and elevated it to a new favorite!</p>
    </div>
    <div class="item" style="left:314px;top:536px;width:250px;">
      <h3>Pub Style Nachos <span class="price">14</span></h3>
      <p>Heaps of fresh corn chips topped with a generous helping of tomatoes, green pepper, red onions, black olives, jalapeno peppers, and warm, house blend of melted cheese, served with a fresh homemade salsa and sour cream.</p>
      <p class="note">Add chicken 4</p>
    </div>
    <div class="item" style="left:314px;top:640px;width:250px;">
      <h3>Brackenfeld's Seafood &amp;Spinach Dip <span class="price">15</span></h3>
      <p>This rich and satisfyingly gooey dip is the perfect blend of seafood and cheese! Served warm with corn chips and fried naan bread. This is a favorite dish. Go ahead and indulge!</p>
    </div>
  </section>

  <h2 class="section-title main">-MAIN-</h2>

  <section class="main-col">
    <div class="item" style="left:638px;top:82px;">
      <h3>Harbourline Beer Battered Fish and Chips <span class="price">16</span></h3>
      <p>We've paired two local legends; Irish lager and a fresh fillet, we've lightly battered it and we're serving it up with thick cut fries, our own "Chi-side" slaw and a serving of homemade tartar sauce.</p>
    </div>
    <div class="item" style="left:638px;top:178px;">
      <h3>Trinity Bay Fish Cakes <span class="price">12</span></h3>
      <p>Our cakes are made the traditional way; with salt cod. Staying with tradition, we're serving them up pan fried not deep fried. Served with side salad and home-made chow chow.</p>
    </div>
    <div class="item" style="left:638px;top:254px;">
      <h3>Matilda's Pan Seared Haddock <span class="price">14</span></h3>
      <p>Our generous haddock fillet is lightly floured and pan seared to golden brown. Served with buttery mash and seasonal veg with a side of our homemade tartar sauce.</p>
    </div>
    <div class="item" style="left:638px;top:349px;">
      <h3>Planked Salmon with Maple Mustard and Whiskey Sauce <span class="price">20</span></h3>
      <p>A flakey fillet of salmon, slow roasted on a cedar plank then topped with a delectable maple mustard and whiskey sauce. Served with our battery mash and fresh seasonal veg.</p>
    </div>
    <div class="item" style="left:638px;top:458px;">
      <h3>Traditional Corned Beef and Cabbage <span class="price">14</span></h3>
      <p>Having memories of comfort food and a home cooked dinner? Look no further than this rich and tasty and savory combination. Just like grandma made.</p>
    </div>
    <div class="item" style="left:638px;top:549px;">
      <h3>Chicken Pot Pie <span class="price">14</span></h3>
      <p>Comfort food at its finest! Our creamy pot pie has tender chunks of chicken, carrots, and peas all smothered in a rich, tasty sauce, topped with a buttery biscuit crust. Served with a farmer's salad</p>
    </div>
    <div class="item" style="left:638px;top:634px;">
      <h3>Ribeye Steak <span class="price">25</span></h3>
      <p>We take a peak of tenderness, aged and trimmed 12oz AAA ribeye, high-temp char-broil it to your exact specifications and let the steak do the talking. Served with grilled vegetables, your choice of side and grilled artisan potato bread</p>
    </div>

    <div class="item" style="left:912px;top:82px;width:260px;">
      <h3>Tikka Curry <span class="price">15</span></h3>
      <p>Take an awesome blend of pulled chicken and fresh garden vegetables and slow cook them in a flavor filled house made curry sauce. This dish is pleasantly aromatic and not overly spicy (we can amp it up if you like). Served with naan and over a bed of basmati rice.</p>
    </div>
    <div class="item" style="left:912px;top:180px;width:260px;">
      <h3>Dubliner Chicken <span class="price">17</span></h3>
      <p>A local favorite! Fresh, tender chicken breast chock-full with a savory apple and onion stuffing smothered in a white wine sauce. Served with buttery champ and seasonal vegetable medley.</p>
    </div>
    <div class="item" style="left:912px;top:264px;width:260px;">
      <h3>Irish Shepherd's Pie <span class="price">15</span></h3>
      <p>A flavorful combination of braised beef and pork simmered in a demi-glace with traditional veg then topped with champ and slow baked to golden brown perfection. Served with a farmer's salad.</p>
    </div>
    <div class="item" style="left:912px;top:349px;width:260px;">
      <h3>Bangers and Mash <span class="price">14</span></h3>
      <p>Two juicy sausages served on top of our homemade buttery champ, sauerkraut then smothered in a mouth-watering maple whiskey sauce.</p>
    </div>
    <div class="item" style="left:912px;top:424px;width:260px;">
      <h3>Brackenfeld's Burger* <span class="price">15</span></h3>
      <p>This is one bangin' burger! One half-pound all beef patty topped with double smoked bacon, spinach, red onion, tomato, dark stout cheese, our special Lady Ashgrove relish and a fried egg on a potato-bread bun. Served with thick cut fries and our "Chi-side" slaw.</p>
    </div>
    <div class="item" style="left:912px;top:528px;width:260px;">
      <h3>Bacon Cheddar Burger <span class="price">14</span></h3>
      <p>A massive juicy half-pound all beef patty topped with three-blend cheese and smoked bacon. It's straightforward and to the point awesomeness on a potato-bread bun.</p>
    </div>
  </section>

  <h2 class="section-title sides">SIDES</h2>
  <ul class="sides-list">
    <li>Garden Salad 4</li>
    <li>Chi-side Slaw 3</li>
    <li>Side of Thick Cut Fries 5</li>
    <li>Baked Beans 4</li>
    <li>Champ 4</li>
    <li>Dark Stout Gravy 3</li>
  </ul>
</main>
</body>
</html>
```